Flex Forward Thaw 21 day Challenge

We are having a Flex Forward Thaw Challenge at our fitness studio. We need a poster design using the template attached as a reference. I have also included our Molvaro logo to put on the poster. Please DO NOT use the graphics in the flyer as we are expecting something much better :-)

-Size needed 11x17 with bleeding for printing

-We need this made in Photoshop (CS3 friendly) or at least delivered in PS as we might change some text or re-arrange the design later on.

-We need this in layers.

```html
<!DOCTYPE html>
<html lang="en">
<head>
<meta charset="utf-8">
<title>Flex Forward Thaw 21 day Challenge</title>
<link rel="stylesheet" href="https://fonts.googleapis.com/css2?family=Oswald:wght@700&family=Titillium+Web:ital,wght@1,300&family=Didact+Gothic&display=swap">
<style>
  :root {
    --red: #ee3124;
    --ink: #111111;
    --white: #ffffff;
    --charcoal: #232323;
    --charcoal-deep: #1a1a1a;
    --photo-light: #d9d9d9;
    --photo-mid: #9a9a9a;
    --photo-dark: #555555;
    --band: rgba(90, 90, 90, 0.82);
  }
  * { margin: 0; padding: 0; box-sizing: border-box; }
  html, body { width: 777px; height: 1200px; overflow: hidden; background: var(--charcoal); }
  .poster {
    position: relative;
    width: 777px;
    height: 1200px;
    overflow: hidden;
    background: radial-gradient(ellipse at 50% 60%, #2c2c2c 0%, var(--charcoal) 55%, var(--charcoal-deep) 100%);
    font-family: "Didact Gothic", sans-serif;
    color: var(--white);
  }
  .hero-photo {
    position: absolute; left: 0; top: 0; width: 777px; height: 458px;
    background: linear-gradient(100deg, var(--photo-light) 0%, #c4c4c4 40%, var(--photo-mid) 65%, var(--photo-dark) 100%);
  }
  .headline {
    position: absolute; left: 44px; top: 8px;
    font-family: "Oswald", sans-serif; font-weight: 700;
    text-transform: uppercase; line-height: 0.98; color: var(--ink);
  }
  .headline span { display: block; }
  .headline .line-1 { font-size: 76px; }
  .headline .line-2 { font-size: 86px; }
  .headline .line-3 { font-size: 92px; }
  .accent { color: var(--red); }
  .tagline-band {
    position: absolute; left: 0; top: 310px; width: 777px; height: 148px;
    background: var(--band);
  }
  .tagline {
    position: absolute; left: 0; top: 322px; width: 777px;
    text-align: center;
    font-family: "Titillium Web", sans-serif; font-style: italic; font-weight: 300;
    font-size: 36px; line-height: 54px; letter-spacing: 0.5px;
  }
  .tagline .first { display: block; padding-left: 20px; }
  .tagline .second { display: block; padding-left: 10px; }
  .brand {
    position: absolute; left: 22px; top: 472px; width: 374px; height: 102px;
    display: flex; align-items: center; justify-content: center; gap: 14px;
    font-size: 44px; letter-spacing: 6px; text-transform: uppercase; color: var(--white);
  }
  .brand-mark { width: 22px; height: 22px; background: var(--red); }
  .icon { position: absolute; }
  .feature {
    position: absolute; width: 176px; text-align: center;
    font-size: 22px; line-height: 33px; letter-spacing: 0.5px;
  }
  .feature-coach { left: 36px; top: 692px; }
  .feature-nutrition { left: 234px; top: 698px; }
  .feature-training { left: 418px; top: 570px; }
  .feature-session { left: 591px; top: 572px; }
  .offer-bar {
    position: absolute; left: 24px; top: 922px; width: 730px; height: 104px;
    background: var(--red);
    display: flex; align-items: center; justify-content: center;
    font-size: 26px; letter-spacing: 0.5px;
  }
  .testimonial { position: absolute; left: 24px; top: 1056px; width: 364px; height: 116px; }
  .testimonial svg { position: absolute; left: 0; top: 0; }
  .quote { position: absolute; left: 30px; top: 18px; font-size: 21px; line-height: 26px; letter-spacing: 0.5px; }
  .quote-author { position: absolute; right: 22px; top: 76px; font-size: 18px; letter-spacing: 0.5px; }
  .call-to-action {
    position: absolute; left: 420px; top: 1058px; width: 340px; text-align: center;
    font-family: "Titillium Web", sans-serif; font-style: italic; font-weight: 300;
    font-size: 19px; line-height: 28px; text-transform: uppercase; letter-spacing: 0.8px;
  }
  .call-to-action .contact { display: block; margin-top: 6px; color: var(--red); font-size: 20px; }
</style>
</head>
<body>
<main class="poster">
  <div class="hero-photo" role="img" aria-label="Black and white photo of a muscular athlete doing push-ups on kettlebells in a gym"></div>

  <h1 class="headline">
    <span class="line-1"><span class="accent" style="display:inline">Flex</span></span>
    <span class="line-2">Forward</span>
    <span class="line-3 accent">Thaw</span>
  </h1>

  <div class="tagline-band"></div>
  <p class="tagline"><span class="first">Discover the Secret to a Beach-Ready</span><span class="second">Body in Just 21 Days!</span></p>

  <div class="brand"><span class="brand-mark"></span>Molvaro</div>

  <svg class="icon icon-dumbbell" style="left:470px;top:480px" width="76" height="76" viewBox="0 0 76 76" aria-hidden="true">
    <g fill="#fff" transform="rotate(-45 38 38)">
      <rect x="6" y="34" width="64" height="8" rx="2"/>
      <rect x="12" y="22" width="8" height="32" rx="2"/>
      <rect x="22" y="18" width="8" height="40" rx="2"/>
      <rect x="46" y="18" width="8" height="40" rx="2"/>
      <rect x="56" y="22" width="8" height="32" rx="2"/>
    </g>
  </svg>

  <svg class="icon icon-calendar" style="left:640px;top:478px" width="78" height="78" viewBox="0 0 78 78" aria-hidden="true">
    <rect x="4" y="10" width="70" height="64" rx="6" fill="none" stroke="#fff" stroke-width="6"/>
    <rect x="4" y="10" width="70" height="14" fill="#fff"/>
    <rect x="18" y="2" width="7" height="16" rx="2" fill="#fff"/>
    <rect x="53" y="2" width="7" height="16" rx="2" fill="#fff"/>
    <rect x="35" y="32" width="8" height="22" rx="2" fill="#fff"/>
    <circle cx="39" cy="62" r="4.5" fill="#fff"/>
  </svg>

  <svg class="icon icon-arm" style="left:80px;top:596px" width="84" height="72" viewBox="0 0 84 72" aria-hidden="true">
    <path fill="#fff" d="M6 66 C4 46 10 22 24 8 C30 2 40 2 42 8 C44 14 38 18 32 18 C28 26 28 34 30 40 C38 30 54 28 66 34 C80 40 82 56 74 64 C64 72 30 72 6 66 Z"/>
  </svg>

  <svg class="icon icon-nutrition" style="left:268px;top:594px" width="82" height="78" viewBox="0 0 82 78" aria-hidden="true">
    <rect x="52" y="2" width="18" height="10" rx="2" fill="#fff"/>
    <path fill="#fff" d="M48 16 H74 V72 C74 75 72 77 69 77 H53 C50 77 48 75 48 72 Z"/>
    <circle cx="28" cy="50" r="26" fill="#fff"/>
    <path fill="#232323" d="M28 26 L32 34 L40 30 L35 38 L42 42 L32 41 L28 48 L24 41 L14 42 L21 38 L16 30 L24 34 Z"/>
  </svg>

  <p class="feature feature-coach">Your very own Personal Accountability Coach to ensure you get results</p>
  <p class="feature feature-nutrition">21 days of nutritional guidance, including delicious recipes</p>
  <p class="feature feature-training">9 total training sessions designed to incinerate fat off your midsection, thighs, and arms</p>
  <p class="feature feature-session">A Success Session to map out your individual plan for success</p>

  <div class="offer-bar">You get all this (a $399 value) for ONLY $99!</div>

  <figure class="testimonial">
    <svg width="364" height="116" viewBox="0 0 364 116" aria-hidden="true">
      <g fill="none" stroke="#ee3124" stroke-width="5">
        <path d="M10 26 V3 H30"/>
        <path d="M332 3 H361 V34"/>
        <path d="M10 84 V113 H30"/>
        <path d="M334 113 H361 V84"/>
      </g>
    </svg>
    <blockquote class="quote">I’ve never been more fit in<br>my life — at age 41!</blockquote>
    <figcaption class="quote-author">~Marisol Brantley</figcaption>
  </figure>

  <p class="call-to-action">Hurry! Space is limited to only<br>20 participants!!!<br>Claim your spot now:<span class="contact">Website and phone number</span></p>
</main>
</body>
</html>
```